Web application design for investigative software

ClueVane is an investigation web application that would organize, create visualizations and allow collaboration. It’s available to anyone and can be used by students, historians, watchdog groups, civic hackers, investigative reporters, mystery enthusiasts, authors, even conspiracy theorists.

We are looking for two related pages. The first, a splash, or front, page and the second a ‘template’ for the web application. They should both be styled the same. The only restriction is that the logo is set.

The design should also be modern and visually well organized — employing a combination of visual devices and info graphics. Keep it light and not too heavy but strong/ professional. Do not be influenced by the current colors of cluevane-example.com, though the colors should be compatible with the logo..

The pages should be compatible with bootstrap, mostly for it’s JS and component functionality. It can be advised by the designer that a subset of bootstrap be used.

The splash page.
Something along the lines of (though not a copy of) :
https://www.plorvex-example.com/advertise
http://www.brimtallhost-example.net/
http://www.corvilode-example.com/
http://www.fennaquist-example.com/

I have a very rough wire frame ish html file uploaded. Use a a guide, but alternate ideas are encouraged.

The application page should have some sort of bar for at the top for system level links a header and a footer. A vertical column to the left between the header and footer for ads, though this will be dynamic as a user can pay out of seeing adds. All dynamic actions will be made by the developers at ClueVane.

WARNING. Please do not submit pre-made templates from some template website. We can do that ourselves for free.

This project will deliver CODE. HTML, CSS and supporting graphics and files.

```html
<!DOCTYPE html>
<html lang="en">
<head>
<meta charset="utf-8">
<title>ClueVane</title>
<link rel="stylesheet" href="https://fonts.googleapis.com/css2?family=Open+Sans:wght@400;600&family=Roboto+Condensed:wght@400&display=swap">
<style>
  :root{
    --red:#c81e22;
    --red-dark:#9c1216;
    --red-deep:#7e0c10;
    --ink:#333;
    --ink-soft:#4a4a4a;
    --white:#fff;
    --footer:#f2f2f2;
  }
  *{box-sizing:border-box;margin:0;padding:0}
  html,body{width:825px;height:1200px;overflow:hidden;background:var(--white)}
  body{position:relative;font-family:"Open Sans",Arial,sans-serif;color:var(--ink)}
  .cond{font-family:"Roboto Condensed","Arial Narrow",sans-serif}

  /* Header */
  .site-header{position:absolute;left:0;top:0;width:825px;height:205px;background:var(--red-dark)}
  .header-panel{position:absolute;left:8px;top:0;width:809px;height:214px;
    background:linear-gradient(#fafafa,#d9d9d9);border-radius:0 0 10px 10px}
  .brand-bubble{position:absolute;left:8px;top:14px;width:140px;height:140px;border-radius:50%;
    background:linear-gradient(#fdfdfd,#ececec)}
  .brand{position:absolute;left:52px;top:51px;display:flex;align-items:center;gap:18px}
  .brand-mark{width:34px;height:34px;border-radius:50%;background:var(--red)}
  .brand-name{font-size:28px;font-weight:600;color:var(--red);line-height:1}

  .top-nav{position:absolute;left:564px;top:17px;height:39px;display:flex;
    border-radius:3px;overflow:hidden;box-shadow:0 3px 4px rgba(0,0,0,.3)}
  .top-nav a{display:block;padding:0 18px;line-height:39px;color:var(--white);
    text-decoration:none;font-size:16px;background:linear-gradient(#3a3a3a,#232323)}
  .top-nav a.is-active{background:linear-gradient(#d4262a,#a8161a)}

  .header-tab{position:absolute;top:144px;height:47px;line-height:47px;color:var(--white);
    font-size:19.5px;background:linear-gradient(#444,#2b2b2b);padding:0 17px;white-space:nowrap}
  .header-tab--left{left:0;width:445px;padding-left:25px;border-radius:0 3px 3px 0}
  .header-tab--right{left:518px;width:307px;border-radius:3px 0 0 3px}

  /* Hero */
  .hero{position:absolute;left:0;top:205px;width:825px;height:274px;
    background:linear-gradient(#4a4a4a,#1f1f1f)}
  .ribbon-tail{position:absolute;top:42px;width:40px;height:62px;background:var(--red-deep)}
  .ribbon-tail--left{left:32px;clip-path:polygon(0 0,100% 0,100% 100%,0 100%,18% 50%)}
  .ribbon-tail--right{left:756px;clip-path:polygon(0 0,100% 0,82% 50%,100% 100%,0 100%)}
  .ribbon{position:absolute;left:63px;top:26px;width:701px;height:70px;text-align:center;
    color:var(--white);background:linear-gradient(#d52a2e,#b8191d);box-shadow:0 2px 4px rgba(0,0,0,.35)}
  .ribbon h1{font-weight:400;font-size:22px;margin-top:9px}
  .ribbon p{font-size:14.5px;margin-top:6px}
  .feature{position:absolute;top:96px;width:198px;height:151px;text-align:center;color:var(--white);
    background:linear-gradient(#d02428,#b61a1e)}
  .feature h2{font-weight:400;font-size:22px;margin-top:10px}
  .feature svg{display:block;margin:12px auto 0}
  .feature--organize{left:90px}
  .feature--visualize{left:315px}
  .feature--collaborate{left:539px}

  /* Content */
  .content{position:absolute;left:8px;top:479px;width:809px;height:649px;background:var(--white)}
  .content-inner{padding:18px 30px 0 18px}
  .content p{font-size:13.2px;line-height:21px;color:var(--ink-soft);margin-bottom:9px}
  .section-tab{height:47px;line-height:47px;width:301px;margin:25px 0 13px -18px;padding-left:22px;
    color:var(--white);font-size:19.5px;font-weight:400;background:linear-gradient(90deg,#3d3d3d,#262626);
    border-radius:0 3px 3px 0}
  .section-tab--get{margin-top:36px}

  /* Footer */
  .site-footer{position:absolute;left:8px;top:1128px;width:809px;height:72px;background:var(--footer)}
  .footer-links{position:absolute;left:17px;top:16px;font-size:12.5px;color:var(--ink)}
  .footer-links a{color:var(--ink);text-decoration:none}
  .footer-links a.is-current{color:var(--red)}
  .footer-links .sep{color:#aaa;margin:0 5px}
  .copyright{position:absolute;left:17px;top:42px;font-size:12.5px}
  .social{position:absolute;left:425px;top:28px;display:flex;gap:7px}
  .social span{width:21px;height:21px;border-radius:3px;background:#3b5b99}
  .social span:first-child{background:#333}
  .social span:last-child{background:#3aa1c9}
  .footer-brand{position:absolute;left:632px;top:16px;display:flex;align-items:center;gap:20px}
  .footer-brand .brand-mark{width:30px;height:30px}
  .footer-brand .brand-name{font-size:23px}
</style>
</head>
<body>

<header class="site-header">
  <div class="header-panel"></div>
  <div class="brand-bubble"></div>
  <div class="brand"><span class="brand-mark"></span><span class="brand-name">ClueVane</span></div>

  <nav class="top-nav cond">
    <a href="#" class="is-active">About Us</a>
    <a href="#">Register</a>
    <a href="#">Sign In</a>
  </nav>

  <div class="header-tab header-tab--left cond">Use ClueVane to plot a novel, or to investigate a crime</div>
  <div class="header-tab header-tab--right cond">ClueVane’s graphical analysis tools</div>
</header>

<section class="hero">
  <div class="ribbon-tail ribbon-tail--left"></div>
  <div class="ribbon-tail ribbon-tail--right"></div>
  <div class="ribbon cond">
    <h1>ClueVane allows You</h1>
    <p>to easily visualize people, events, things, groups, and timelines &amp; to easily see the relationships between them.</p>
  </div>

  <div class="feature feature--organize cond">
    <h2>Organize</h2>
    <svg width="90" height="86" viewBox="0 0 90 86" aria-hidden="true">
      <rect x="4" y="4" width="64" height="78" fill="none" stroke="#fff" stroke-width="6"/>
      <g stroke="#fff" stroke-width="6"><line x1="16" y1="24" x2="54" y2="24"/><line x1="16" y1="38" x2="46" y2="38"/><line x1="16" y1="52" x2="36" y2="52"/><line x1="16" y1="66" x2="30" y2="66"/></g>
      <polygon points="76,26 88,38 50,76 36,80 40,66" fill="#fff"/>
    </svg>
  </div>

  <div class="feature feature--visualize cond">
    <h2>Vistualize</h2>
    <svg width="116" height="80" viewBox="0 0 116 80" aria-hidden="true">
      <path d="M4 40 Q58 -16 112 40 Q58 96 4 40Z" fill="none" stroke="#fff" stroke-width="6"/>
      <circle cx="58" cy="40" r="22" fill="none" stroke="#fff" stroke-width="6"/>
      <circle cx="58" cy="40" r="10" fill="#fff"/>
    </svg>
  </div>

  <div class="feature feature--collaborate cond">
    <h2>Colaborate</h2>
    <svg width="100" height="86" viewBox="0 0 100 86" aria-hidden="true">
      <path d="M50 84 L10 44 A24 24 0 0 1 50 12 A24 24 0 0 1 90 44Z" fill="#fff"/>
    </svg>
  </div>
</section>

<main class="content">
  <div class="content-inner">
    <p>Have you ever compiled a lot of data about something, but been unable to figure out what it means? Often, the number of people involved, the number of events at which they might have met, and the number of common contacts are just too much for a person to track. This can happen when you are trying to understand the players and interests in current events, or the characters and actions in a novel. It’s easy to collect the data, but hard to visualize it&nbsp; or analyze the relationships.</p>
    <p>This is where ClueVane comes in. ClueVane allows you to easily visualize people, events, things, groups, and timelinesand to easily see the relationships between them.</p>
    <p>Use ClueVane to plot a novel, or to investigate a crime. Use it to analyze your favorite conspiracy theory and look for relationships that have eluded the investigators. Use it to track the causes and results of historical events – or current ones. Use it to track changing relationships among your friends at high school. Use it to track the twists and turns of a role-playing game. There’s no end to what you can investigate with ClueVane</p>

    <h2 class="section-tab cond">How does ClueVane work?</h2>
    <p>Once data has been entered, use ClueVane’s graphical analysis tools to analyze your data in new ways. Use relationship maps to find out how two people or groups are associated. Use timeline analysis to show cause and effect of seemingly unrelated events. Use social network mapping to show how relationships change over time. Look for events that stand out or relationships that have great impact on multiple events. Like a spider’s web, look for the intersections that matter, then look for the players that brought that intersection into focus.</p>

    <h2 class="section-tab section-tab--get cond">What do I get with ClueVane?</h2>
    <p>Basic ClueVane will allow any registered user to create, maintain and analyze one investigation. Advanced features will be available a la carte and will include special analytical reports, multiple investigations, and the ability to share an investigation among multiple users. Investigations of general interest could also be shared publicly in read-only mode.</p>
    <p>You will also get access to several read-only public investigations to use as a model. These might include the plots of popular novels or movies, the details of a major political event, or an investigation into a famous crime.</p>
  </div>
</main>

<footer class="site-footer">
  <nav class="footer-links">
    <a href="#" class="is-current">Home</a><span class="sep">/</span>
    <a href="#">About us</a><span class="sep">/</span>
    <a href="#">Register</a><span class="sep">/</span>
    <a href="#">Sign In</a><span class="sep">/</span>
    <a href="#">Contact us</a>
  </nav>
  <div class="copyright">Copyright &nbsp;© 2014 ClueVane . All rights reserved.</div>
  <div class="social" aria-label="Social links"><span></span><span></span><span></span></div>
  <div class="footer-brand"><span class="brand-mark"></span><span class="brand-name">ClueVane</span></div>
</footer>

</body>
</html>
```